Corvane Electrical Solutions

On one side. LOGO (underneath:) Commercial Industrial Residential

- NAME & CONTACT DETAILS

Marcus T. Hollings
Project Manager

(Cell icon) (441) 582-6197
(Email icon) cvnelectricalsoultions@mailventra.com
(Facebook & Instagram icons )@cvnelectricalsolutions

Other side: LOGO - underneath ELECTRICAL CONSTRUCTION & MAINTENANCE . LED LIGHTING & AUTOMATION . LIFE SAFETY SYSTEMS (FIRE ALARM / SECURITY) . DATA & COMMUNICATION

```html
<!DOCTYPE html>
<html lang="en">
<head>
<meta charset="utf-8">
<title>Corvane Electrical Solutions – Business Card</title>
<link href="https://fonts.googleapis.com/css2?family=Montserrat:wght@400;500;600;700&family=Lexend:wght@600&display=swap" rel="stylesheet">
<style>
  :root {
    --teal: #04506a;
    --ink: #2f2f2f;
    --mute: #4a4a4a;
    --ghost: #dcdcdc;
    --paper: #ffffff;
    --shadow-light: #a9a9a9;
    --shadow-dark: #2a2a2a;
  }
  * { box-sizing: border-box; margin: 0; padding: 0; }
  html, body { width: 1200px; height: 1200px; overflow: hidden; background: var(--paper); }
  body { position: relative; font-family: "Montserrat", sans-serif; }

  .card { position: absolute; left: 220px; width: 760px; height: 456px; overflow: hidden; }
  .card-front { top: 124px; background: var(--paper); border: 1px solid var(--ink); box-shadow: 4px 4px 0 var(--shadow-light); overflow: visible; }
  .card-back { top: 620px; background: var(--teal); border: 1px solid var(--shadow-dark); box-shadow: 4px 4px 0 var(--shadow-dark); }

  .brand { position: absolute; display: flex; align-items: center; gap: 14px; }
  .brand-mark { width: 58px; height: 58px; background: var(--teal); }
  .brand-name { font-weight: 500; font-size: 22px; line-height: 1.12; letter-spacing: 3px; color: var(--teal); text-transform: uppercase; }
  .front-brand { left: 55px; top: 80px; }
  .back-brand { left: 0; right: 0; top: 162px; justify-content: center; }
  .back-brand .brand-mark { background: var(--paper); width: 72px; height: 72px; }
  .back-brand .brand-name { color: var(--paper); font-size: 25px; }

  .sectors { position: absolute; left: 55px; top: 190px; font-family: "Lexend", sans-serif; font-weight: 600; font-size: 24px; color: var(--teal); letter-spacing: -0.2px; }

  .person { position: absolute; left: 55px; top: 247px; }
  .person-name { font-weight: 700; font-size: 24.5px; color: var(--teal); line-height: 1.1; }
  .person-role { font-weight: 400; font-size: 18px; color: var(--mute); line-height: 1.1; }

  .contacts { position: absolute; left: 55px; top: 303px; list-style: none; }
  .contacts li { display: flex; align-items: center; gap: 7px; height: 23px; font-size: 15px; color: var(--ink); }
  .contacts svg { width: 16px; height: 16px; flex: none; }
  .contacts .handle { font-weight: 700; }
  .social-square { width: 15px; height: 15px; background: var(--teal); flex: none; }

  .pin { position: absolute; left: 521px; top: 308px; width: 27px; height: 32px; }
  .address { position: absolute; left: 480px; top: 346px; font-size: 13.5px; line-height: 19px; color: var(--ink); }

  .ghost-name { position: absolute; left: 600px; top: 228px; width: 380px; transform: translate(-50%, -50%) rotate(90deg); transform-origin: center; margin-left: 58px; font-weight: 700; font-size: 72px; letter-spacing: 2px; color: var(--ghost); text-align: center; line-height: 1; white-space: nowrap; }

  .services { position: absolute; left: 0; right: 0; top: 282px; text-align: center; color: var(--paper); font-weight: 700; font-size: 14px; line-height: 22px; }
</style>
</head>
<body>

<section class="card card-front">
  <div class="brand front-brand">
    <span class="brand-mark"></span>
    <span class="brand-name">Corvane<br>Electrical<br>Solutions</span>
  </div>

  <p class="sectors">Commercial Industrial Residential</p>

  <div class="person">
    <p class="person-name">Marcus T. Hollings</p>
    <p class="person-role">Project Manager</p>
  </div>

  <ul class="contacts">
    <li>
      <svg viewBox="0 0 16 16" aria-hidden="true"><rect x="3" y="1" width="10" height="14" rx="2" fill="none" stroke="#04506a" stroke-width="1.8"/><circle cx="8" cy="12.2" r="0.9" fill="#04506a"/></svg>
      <span>(441) 582-6197</span>
    </li>
    <li>
      <svg viewBox="0 0 16 16" aria-hidden="true"><rect x="1" y="3" width="14" height="10" fill="none" stroke="#04506a" stroke-width="1.6"/><path d="M1 3 L8 9 L15 3 M1 13 L6 7.5 M15 13 L10 7.5" fill="none" stroke="#04506a" stroke-width="1.4"/></svg>
      <span>cvnelectricalsoultions@mailventra.com</span>
    </li>
    <li>
      <span class="social-square"></span>
      <span class="handle">@cvnelectricalsolutions</span>
    </li>
  </ul>

  <svg class="pin" viewBox="0 0 27 32" aria-hidden="true"><path d="M13.5 1 C6.6 1 1.5 6.1 1.5 12.6 C1.5 20 13.5 31 13.5 31 C13.5 31 25.5 20 25.5 12.6 C25.5 6.1 20.4 1 13.5 1 Z" fill="#04506a"/><circle cx="13.5" cy="12.5" r="4.6" fill="#ffffff"/></svg>
  <p class="address">PO BOX HM 318<br>Hamilton,HM BX<br>BERMUDA</p>

  <div class="ghost-name" aria-hidden="true">CORVANE</div>
</section>

<section class="card card-back">
  <div class="brand back-brand">
    <span class="brand-mark"></span>
    <span class="brand-name">Corvane<br>Electrical<br>Solutions</span>
  </div>
  <p class="services">
    ELECTRICAL CONSTRUCTION &amp; MAINTENANCE,<br>
    LED LIGHTING&amp; AUTOMATION, LIFE SAFETY SYSTEMS(FIRE ALARM/SECURITY),<br>
    DATA&amp; COMMUNICATION
  </p>
</section>

</body>
</html>
```